Plimsoo car advertisement

de website moet uit minimaal 3 pagina's bestaan. 1 pagina als een landingspagina. 1 pagina voor consumenten die hun auto willen laten beplakken met bedrijfsreclame en 1 pagina voor bedrijven / consumenten die hun bedrijfsreclame op een consumentenauto wilt plaatsen.

de website moet echt een happy website zijn. consumenten kunnen geld verdienen met reclame op hun auto te laten zetten en bedrijven kunnen voor een relatief goedkoop bedrag hun bedrijfsreclame op een auto laten zetten. die auto rijdt dan rond en veel mensen zien de reclame.

beide pagina's moeten dus een glimlach opleveren.

het doel van de startpagina is dat je door kunt gaan naar de consumenten en de bedrijfspagina.

gebruik leuke, vrolijke kleuren en vormen en zorg dat de mensen een glimlach krijgen als ze naar de website kijken.

doelgroep is consumenten die een auto rijden en geld willen verdienen met hun auto en de zakelijke ondernemer die voor een goedkoop bedrag zijn bedrijfsreclame met een full carwrap kan laten zien aan de buitenwereld.

doordat consumenten zich bij ons aanmelden hebben wij een database met auto's en weten we hoeveel deze auto's rijden en in welke regio's ze rijden en wat voor auto ze rijden. allemaal hele belangrijke informatie voor een ondernemer die reclame wilt maken op ene specifieke auto type en in een bepaalde regio.

-

website should consist of at least 3 pages. 1 landing page, 1 customer page and 1 business page. landing page let's the visitor choose wether he / she is a customer with a car and wants to allow his car to be fully carwrapped or he / she is a business owner who wants to place his advertisement on a car.

website should be a really happy joyfull website and bring a smile to the visitor. beause the customer can earn money (200 euro / month nett) by allowing advertisements on his car (full car wrap) and the business owner because for a low price he can advertise.

when customers that owns a car register themselves with our website we build a database with cars in specific locations. a business owner wants to advertise his product into a specific region. this is very valuable information.

agreement is 1 year for a customer to have advertisements on his car and for a business to advertise. after that year, the advertisements are safely removed from the car and new advertisement agreements can be made. a business can place advertisements (full carwrap) already for 795 euro's., Details for my new Web Design Project will be added soon. , de website moet uit minimaal 3 pagina's bestaan. 1 pagina als een landingspagina. 1 pagina voor consumenten die hun auto willen laten beplakken met bedrijfsreclame en 1 pagina voor bedrijven / consumenten die hun bedrijfsreclame op een consumentenauto wilt plaatsen.

Target Market(s)

customers who has a car
businesses who want to advertise their business / product on a car

Industry/Entity Type

Business

Requirements
Must have
• website should be playfull, colorfull and a joy to look at and work with. altough functoinality is very limited visitors need to be intrigued to proceed to contact plimsoo.
Nice to have
• nice graphics, moving images, a "living" website (not so static)

```html
<!DOCTYPE html>
<html lang="en">
<head>
<meta charset="utf-8">
<title>Plimsoo – Car Advertisement</title>
<link href="https://fonts.googleapis.com/css2?family=Arimo:ital,wght@0,400;0,700;1,400&display=swap" rel="stylesheet">
<style>
  :root {
    --orange: #f7941d;
    --red: #e0252a;
    --white: #ffffff;
    --ink: #666666;
    --dark-panel: rgba(0, 0, 0, 0.82);
    --hero-box: rgba(40, 40, 40, 0.72);
    --rule: #8a8a8a;
  }
  * { box-sizing: border-box; margin: 0; padding: 0; }
  html, body { width: 1200px; height: 628px; overflow: hidden; }
  body {
    position: relative;
    font-family: "Arimo", Arial, sans-serif;
    color: var(--white);
    background: #6d6a66;
  }
  .backdrop-photo {
    position: absolute; inset: 0;
    background:
      radial-gradient(ellipse 520px 300px at 600px 360px, #d4d5d8 0%, #b9bbbf 45%, rgba(150,140,130,0) 100%),
      linear-gradient(180deg, #8b8d94 0%, #9a9691 45%, #6f655c 100%);
  }
  .slider-controls {
    position: absolute; top: 8px; right: 10px;
    display: flex; gap: 12px; align-items: center;
  }
  .brand {
    position: absolute; left: 146px; top: 20px;
    font-size: 34px; font-weight: 700; color: var(--orange);
    letter-spacing: -0.5px; line-height: 40px;
  }
  .top-tools {
    position: absolute; left: 911px; top: 16px; width: 145px; height: 44px;
    background: rgba(60, 60, 60, 0.75);
    display: flex; align-items: center; padding-left: 20px; gap: 8px;
  }
  .top-tools .divider { width: 1px; height: 20px; border-left: 1px dotted #bbb; margin: 0 4px; }
  .social-dot { width: 14px; height: 14px; border-radius: 50%; background: var(--white); }
  .top-rule {
    position: absolute; left: 144px; top: 61px; width: 912px; height: 8px;
    background: rgba(70, 70, 70, 0.8);
  }
  .main-nav {
    position: absolute; left: 144px; top: 69px; width: 912px; height: 76px;
    background: var(--white);
    display: flex; align-items: stretch;
  }
  .main-nav a {
    display: flex; align-items: center; padding: 0 14px;
    color: var(--ink); font-size: 13px; text-decoration: none;
  }
  .main-nav a.is-active { background: var(--orange); color: var(--white); width: 61px; justify-content: center; padding: 0; margin-right: 0; }
  .testimonial {
    position: absolute; left: 744px; top: 69px; width: 312px; height: 76px;
    padding: 14px 8px 0 8px;
    background-image: repeating-linear-gradient(135deg, #e2e2e2 0 1px, transparent 1px 4px);
    background-size: 100% 6px; background-repeat: no-repeat;
    background-color: var(--white);
  }
  .testimonial h3 { font-size: 10px; font-weight: 400; color: var(--orange); }
  .testimonial blockquote { font-size: 11px; font-style: italic; color: #888; line-height: 11px; margin-top: 2px; }
  .testimonial cite { display: block; font-size: 10px; font-style: normal; color: #333; margin-top: 3px; }
  .hero-title {
    position: absolute; left: 144px; top: 216px; height: 45px; width: 259px;
    background: var(--hero-box); font-size: 29px; font-weight: 400;
    padding: 6px 13px; line-height: 33px;
  }
  .hero-sub {
    position: absolute; left: 144px; top: 261px; height: 30px; width: 424px;
    background: var(--hero-box); font-size: 13px; padding: 0 13px; line-height: 30px;
  }
  .hero-button {
    position: absolute; left: 144px; top: 300px; width: 95px; height: 33px;
    background: var(--red); color: var(--white); font-size: 11.5px;
    display: flex; align-items: center; justify-content: center; text-decoration: none;
  }
  .site-footer {
    position: absolute; left: 144px; top: 444px; width: 912px; height: 164px;
    background: var(--dark-panel);
  }
  .footer-col { position: absolute; top: 20px; width: 266px; }
  .footer-col h2 {
    font-size: 20px; font-weight: 400; padding-bottom: 4px;
    border-bottom: 1px solid var(--rule); margin-bottom: 6px;
  }
  .footer-col p { font-size: 11.5px; line-height: 16px; }
  .col-about { left: 19px; }
  .col-contact { left: 323px; }
  .col-news { left: 627px; }
  .map-decoration {
    position: absolute; left: 45px; top: 34px; width: 158px; height: 90px;
    border-radius: 40% 50% 45% 40%;
    background: rgba(200, 200, 200, 0.35);
  }
  .contact-line { display: flex; align-items: center; gap: 5px; font-size: 11.5px; position: relative; }
  .newsletter-form { display: flex; margin-top: 20px; }
  .newsletter-form .field { width: 132px; height: 24px; background: #eeeeee; }
  .newsletter-form .submit {
    width: 67px; height: 24px; background: var(--orange); color: var(--white);
    font-size: 11.5px; display: flex; align-items: center; justify-content: center;
  }
  .copyright { position: absolute; left: 19px; top: 140px; font-size: 9px; }
</style>
</head>
<body>
  <div class="backdrop-photo" role="img" aria-label="Photo of a silver compact car with a full advertising wrap, parked on brick paving"></div>

  <div class="slider-controls">
    <svg width="22" height="20" viewBox="0 0 22 20" fill="#c8c8c8"><path d="M1 1h7v3H4v4H1zM21 1h-7v3h4v4h3zM1 19h7v-3H4v-4H1zM21 19h-7v-3h4v-4h3z"/></svg>
    <svg width="18" height="20" viewBox="0 0 18 20" fill="#c8c8c8"><path d="M1 0l17 10L1 20z"/></svg>
    <svg width="40" height="20" viewBox="0 0 40 20" fill="none" stroke="#c8c8c8" stroke-width="3"><path d="M12 2L3 10l9 8M28 2l9 8-9 8"/></svg>
  </div>

  <div class="brand">Plimsoo</div>

  <div class="top-tools">
    <svg width="16" height="11" viewBox="0 0 16 11" aria-label="Nederlands"><rect width="16" height="11" fill="#21468b"/><rect width="16" height="7.3" fill="#fff"/><rect width="16" height="3.7" fill="#ae1c28"/></svg>
    <svg width="16" height="11" viewBox="0 0 16 11" aria-label="English"><rect width="16" height="11" fill="#1f3f8c"/><rect x="6.5" width="3" height="11" fill="#fff"/><rect y="4" width="16" height="3" fill="#fff"/><rect x="7.2" width="1.6" height="11" fill="#c8102e"/><rect y="4.7" width="16" height="1.6" fill="#c8102e"/></svg>
    <span class="divider"></span>
    <span class="social-dot"></span>
    <span class="social-dot"></span>
    <span class="social-dot"></span>
  </div>

  <div class="top-rule"></div>

  <nav class="main-nav">
    <a class="is-active" href="#">Home</a>
    <a href="#">Car Holders</a>
    <a href="#">Business Holders</a>
    <a href="#">Advertisers</a>
    <a href="#">Our Works</a>
    <a href="#">Contact</a>
  </nav>

  <aside class="testimonial">
    <h3>Testimonials</h3>
    <blockquote>"Duis in jus letalis pagus patria verto. Duis eligo facilisis ideo nostrud paratus ulciscor."</blockquote>
    <cite>Jan Verhoef</cite>
  </aside>

  <h1 class="hero-title">Business Holders</h1>
  <p class="hero-sub">For business holders who want to place his advertisement on a car</p>
  <a class="hero-button" href="#">VIEW MORE</a>

  <footer class="site-footer">
    <section class="footer-col col-about">
      <h2>About us</h2>
      <p>Duis in jus letalis pagus patria verto. Duis eligo facilisis ideo nostrud paratus ulciscor. Duis in jus letalis pagus patria verto.</p>
    </section>
    <section class="footer-col col-contact">
      <h2>Contact us</h2>
      <div class="map-decoration" role="img" aria-label="Faint world map decoration"></div>
      <p style="position:relative">Street Address<br>Locality, Region, Netherlands</p>
      <div class="contact-line" style="margin-top:10px">
        <svg width="9" height="14" viewBox="0 0 9 14" fill="none" stroke="#fff" stroke-width="1.4"><rect x="1" y="1" width="7" height="12" rx="1"/><path d="M3.5 11h2"/></svg>
        +31-000-00000
      </div>
      <div class="contact-line" style="margin-top:2px">
        <svg width="12" height="9" viewBox="0 0 12 9" fill="#fff"><rect width="12" height="9"/><path d="M0 0l6 5 6-5" stroke="#000" fill="none"/></svg>
        contact@plimsoo.nl
      </div>
    </section>
    <section class="footer-col col-news">
      <h2>Newsletter</h2>
      <p>Stay informed on our latest news!</p>
      <div class="newsletter-form">
        <span class="field"></span>
        <span class="submit">Subscribe</span>
      </div>
    </section>
    <p class="copyright">© 2013 Plimsoo. All rights reserved</p>
  </footer>
</body>
</html>
```